Harbor Compass - Book Cover

I need a book cover for my debut work, "Harbor Compass - Turning the Tide, One Step at a Time." While the website isn't complete, you can get a sense of what I am writing about by looking at my website, harborcompassbooks.org. The book is a leadership development book, but more of a personal change journey. The emphasis is on figuring out how to combine you work, social, and own self into an authentic package that not only resonates with others, but makes what you achieve more fulfilling.

I am attaching a copy of my logo so you can get a sense of what I like. I would prefer to not have the cover be photographic, but am open to suggestions. This will be a series of books so maintaining some sense of style will be important, and can garner future work.

Industry/Entity Type

Leadership

```html
<!DOCTYPE html>
<html lang="en">
<head>
<meta charset="utf-8">
<title>Harbor Compass – Turning the Tide, One Step at a Time</title>
<link rel="stylesheet" href="https://fonts.googleapis.com/css2?family=Marcellus&display=swap">
<style>
  :root {
    --sky: #66ccf5;
    --royal: #1f5fe8;
    --cyan: #3fbff0;
    --slate: #5f717a;
    --white: #ffffff;
    --paper-light: #fbfbf8;
    --paper-shade: #e4e6e2;
    --gold-light: #f7c650;
    --gold-deep: #e9a423;
    --red-light: #e5392b;
    --red-deep: #c41e14;
    --cream: #fbf5ec;
    --cream-shade: #efe6d8;
    --orange: #e8792a;
  }
  html, body { margin: 0; padding: 0; overflow: hidden; background: var(--sky); }
  .cover {
    position: relative;
    width: 900px;
    height: 1200px;
    overflow: hidden;
    background: var(--sky);
    font-family: "Marcellus", serif;
    color: var(--white);
  }
  .backdrop { position: absolute; inset: 0; width: 900px; height: 1200px; }
  .brand-mark {
    position: absolute;
    top: 70px;
    left: 386px;
    width: 128px;
    height: 128px;
    border-radius: 50%;
    background: var(--royal);
  }
  .title-block {
    position: absolute;
    top: 282px;
    left: 0;
    width: 900px;
    text-align: center;
  }
  .title-block__name {
    margin: 0;
    font-size: 30px;
    font-weight: 400;
    letter-spacing: 1.5px;
  }
  .title-block__tagline {
    margin: 14px 0 0;
    font-size: 58px;
    font-weight: 400;
    line-height: 66px;
    letter-spacing: 3.5px;
  }
  .shelf { position: absolute; inset: 0; }
  .book {
    position: absolute;
    box-shadow: 2px 3px 6px rgba(0,0,0,0.35);
    border: 2px solid var(--white);
    box-sizing: border-box;
  }
  .book--paper { background: linear-gradient(160deg, var(--paper-light) 0%, var(--paper-light) 55%, var(--paper-shade) 100%); }
  .book--one   { left: 2px;   top: 858px; width: 92px;  height: 118px; transform: rotate(-16deg); }
  .book--two   { left: 94px;  top: 775px; width: 106px; height: 160px; transform: rotate(-11deg); }
  .book--three { left: 204px; top: 710px; width: 120px; height: 178px; transform: rotate(-6deg); }
  .book--four  {
    left: 346px; top: 645px; width: 128px; height: 202px; transform: rotate(2deg);
    background: linear-gradient(180deg, var(--gold-light) 0%, var(--gold-deep) 100%);
  }
  .book--five  {
    left: 516px; top: 640px; width: 146px; height: 192px; transform: rotate(1deg);
    background: linear-gradient(180deg, var(--paper-light) 0 14%, var(--red-light) 14%, var(--red-deep) 100%);
  }
  .book--six   {
    left: 682px; top: 640px; width: 200px; height: 204px; transform: rotate(5deg);
    background: linear-gradient(180deg, var(--cream) 0%, var(--cream-shade) 68%, var(--orange) 68% 72%, var(--cream) 72%);
  }
  .site-url {
    position: absolute;
    top: 1110px;
    left: 0;
    width: 900px;
    margin: 0;
    text-align: center;
    font-size: 26px;
    letter-spacing: 1px;
  }
</style>
</head>
<body>
<main class="cover">
  <svg class="backdrop" viewBox="0 0 900 1200" aria-hidden="true">
    <path fill="var(--royal)" d="M0,330 C230,250 560,300 900,228 L900,560 C720,430 420,420 0,520 Z"/>
    <path fill="var(--slate)" d="M0,985 C200,860 560,780 900,760 L900,1200 L0,1200 Z"/>
    <path fill="var(--sky)" d="M0,1015 C240,910 600,865 900,870 L900,1200 L0,1200 Z"/>
    <path fill="var(--cyan)" d="M0,1060 C250,965 600,930 900,945 L900,1200 L0,1200 Z"/>
    <path fill="var(--royal)" d="M0,1100 C260,1020 600,1000 900,1030 L900,1200 L0,1200 Z"/>
    <path fill="#4a86f0" opacity="0.5" d="M0,1190 C300,1120 620,1110 900,1140 L900,1200 L0,1200 Z"/>
  </svg>

  <div class="brand-mark" role="img" aria-label="Harbor Compass brand mark"></div>

  <header class="title-block">
    <p class="title-block__name">Harbor Compass</p>
    <h1 class="title-block__tagline">Turning the Tide,<br>One Step at a Time</h1>
  </header>

  <section class="shelf">
    <div class="book book--paper book--one" role="img" aria-label="Cover of a recommended book on social change"></div>
    <div class="book book--paper book--two" role="img" aria-label="Cover of a recommended book on success"></div>
    <div class="book book--paper book--three" role="img" aria-label="Cover of a recommended book on quick thinking"></div>
    <div class="book book--four" role="img" aria-label="Cover of a recommended family leadership fable"></div>
    <div class="book book--five" role="img" aria-label="Cover of a recommended communication book"></div>
    <div class="book book--six" role="img" aria-label="Cover of a recommended emotional skills book"></div>
  </section>

  <p class="site-url">harborcompassbooks.org</p>
</main>
</body>
</html>
```